Redesign of business card for Birchline Mechanical

We are looking for a new design for our business cards for Birchline Mechanical. We are a plumbing & HVAC construction company, operating on the West Coast of Canada and USA. Logo attached.
Industry/Entity Type
Construction - Plumbing & HVAC
Contact Information for Business Card
Name, address, phone numbers, email, website address
Look and feel
Each slider illustrates characteristics of the customer's brand and the style your logo design should communicate.

```html
<!DOCTYPE html>
<html lang="en">
<head>
<meta charset="utf-8">
<title>Birchline Mechanical — Business Card</title>
<link href="https://fonts.googleapis.com/css2?family=Inter:wght@400;600;700&display=swap" rel="stylesheet">
<style>
  :root {
    --backdrop: #999999;
    --card-dark: #262626;
    --card-light: #ffffff;
    --ink: #111111;
    --muted: #a3a3a8;
    --emboss: #3c3c3c;
  }
  html, body {
    margin: 0;
    padding: 0;
    width: 1200px;
    height: 1000px;
    overflow: hidden;
    background: var(--backdrop);
    font-family: "Inter", Arial, sans-serif;
  }
  .canvas {
    position: relative;
    width: 1200px;
    height: 1000px;
  }
  .card {
    position: absolute;
    left: 293px;
    width: 615px;
    height: 354px;
    border-radius: 18px;
    overflow: hidden;
  }
  .card--front {
    top: 90px;
    background: var(--card-dark);
    display: flex;
    align-items: center;
    justify-content: center;
  }
  .card--back {
    top: 522px;
    background: var(--card-light);
  }
  .front-mark {
    color: var(--emboss);
    font-weight: 700;
    font-size: 34px;
    letter-spacing: 2px;
    text-transform: uppercase;
    text-align: center;
    line-height: 1.1;
  }
  .wordmark {
    position: absolute;
    top: 58px;
    left: 0;
    right: 0;
    text-align: center;
    color: var(--ink);
    font-weight: 700;
    font-size: 22px;
    letter-spacing: 1px;
    line-height: 1.15;
    text-transform: uppercase;
  }
  .person {
    position: absolute;
    top: 200px;
    right: 334px;
    text-align: right;
  }
  .person__name {
    font-weight: 700;
    font-size: 18px;
    color: #000;
    line-height: 22px;
  }
  .person__role {
    font-weight: 600;
    font-size: 16px;
    color: var(--muted);
    line-height: 22px;
  }
  .divider {
    position: absolute;
    left: 296px;
    top: 191px;
    width: 1px;
    height: 59px;
    background: #222;
  }
  .contacts {
    position: absolute;
    left: 312px;
    top: 194px;
    margin: 0;
    padding: 0;
    list-style: none;
  }
  .contacts li {
    display: flex;
    align-items: center;
    height: 17px;
    font-size: 14px;
    color: var(--muted);
  }
  .contacts svg {
    width: 11px;
    height: 11px;
    margin-right: 11px;
    fill: #111;
  }
  .address {
    position: absolute;
    left: 0;
    right: 0;
    top: 310px;
    text-align: center;
    font-size: 14px;
    color: var(--muted);
  }
</style>
</head>
<body>
<div class="canvas">
  <section class="card card--front">
    <div class="front-mark">Birchline<br>Mechanical</div>
  </section>

  <section class="card card--back">
    <div class="wordmark">Birchline<br>Mechanical</div>

    <div class="person">
      <div class="person__name">Name Surname</div>
      <div class="person__role">Position</div>
    </div>

    <div class="divider"></div>

    <ul class="contacts">
      <li>
        <svg viewBox="0 0 24 24" aria-hidden="true"><path d="M6.6 10.8a15.1 15.1 0 0 0 6.6 6.6l2.2-2.2c.3-.3.7-.4 1-.2 1.1.4 2.3.6 3.6.6.6 0 1 .4 1 1V20c0 .6-.4 1-1 1A17 17 0 0 1 3 4c0-.6.4-1 1-1h3.5c.6 0 1 .4 1 1 0 1.3.2 2.5.6 3.6.1.3 0 .7-.2 1z"/></svg>
        213-555-0148
      </li>
      <li>
        <svg viewBox="0 0 24 24" aria-hidden="true"><path d="M2 5h20v14H2zM4 7v.4l8 5.2 8-5.2V7zm0 2.8V17h16V9.8l-8 5.2z"/></svg>
        info@birchlinemech.com
      </li>
      <li>
        <svg viewBox="0 0 24 24" aria-hidden="true"><path d="M12 2a10 10 0 1 0 0 20 10 10 0 0 0 0-20zm6.9 6h-3a15.6 15.6 0 0 0-1.3-3.6A8 8 0 0 1 18.9 8zM12 4c.8 1.2 1.5 2.5 1.9 4h-3.8c.4-1.5 1.1-2.8 1.9-4zM4.3 14a8 8 0 0 1 0-4h3.4a16 16 0 0 0 0 4zm.8 2h3a15.6 15.6 0 0 0 1.3 3.6A8 8 0 0 1 5.1 16zm3-8h-3a8 8 0 0 1 4.3-3.6C8.8 5.6 8.4 6.8 8.1 8zM12 20c-.8-1.2-1.5-2.5-1.9-4h3.8c-.4 1.5-1.1 2.8-1.9 4zm2.3-6H9.7a14.7 14.7 0 0 1 0-4h4.6a14.7 14.7 0 0 1 0 4zm.3 5.6c.6-1.1 1-2.3 1.3-3.6h3a8 8 0 0 1-4.3 3.6zm1.7-5.6a16 16 0 0 0 0-4h3.4a8 8 0 0 1 0 4z"/></svg>
        birchlinemech.com
      </li>
    </ul>

    <div class="address">4120 Harbor View Road, Suite 200, Irvine, CA 92614</div>
  </section>
</div>
</body>
</html>
```